Brellin Trade Partners - we are Asian sourcing agents

We are sourcing agents based in the USA and we act as sourcing agents for clients in throughout the world. We focus primarily on custom sewn goods. So basically companies who do not have the in-house expertise to do it themselves, come to us and have us find suitable factories in Asia to do the production. We are middlemen. We find the factories...quote the project...manage the quality control and then deliver the goods directly to our customer's door. We pride ourselves in making the communication very easy and precise.

Current page is www.brellintrade.example

I am not happy w/ the overall look. The spacing...the photos, the fonts...the design elements...the pictures. I want a cool, crisp design that conveys professionalism and clearly depicts/explains what we do.

Requirements
Must have
• use my logo....I like it...it was designed by someone on this website.
Nice to have
• a video/animation of the entire process would be wonderful. Showing initial contact with our office in the USA...then to my correspondence with my offices in Taiwan and in Hong Kong...and then back and fort w/ the customer.....and then between my people in Hong Kong/Taiwan with the local factories......and then a quote is generated and sent to my client......to samples being made and sent for approval.....to a PO being generated......to final samples being sent.....to the order being shipped and delivered to the clients warehouse. I was thinking of an animation showing arrows and text showing the back and forth communication and explaining how the process flows.

```html
<!DOCTYPE html>
<html lang="en">
<head>
<meta charset="utf-8">
<title>Brellin Trade Partners – Asian Outsourcing Made Easy</title>
<link href="https://fonts.googleapis.com/css2?family=Oswald:wght@400;500&family=Open+Sans:wght@400;600;700&display=swap" rel="stylesheet">
<style>
  :root{
    --navy:#1f2562;
    --navy-deep:#1a1f52;
    --green:#7a9339;
    --green-dark:#6a8130;
    --band:#3c3d82;
    --page:#e9e9ec;
    --white:#ffffff;
    --ink:#2b2b2b;
  }
  *{box-sizing:border-box;margin:0;padding:0}
  html,body{width:730px;height:1200px;overflow:hidden}
  body{position:relative;background:var(--page);font-family:"Open Sans",Arial,sans-serif;color:var(--white)}
  .abs{position:absolute}
  .head{font-family:"Oswald","Arial Narrow",sans-serif;font-weight:500;text-transform:uppercase;letter-spacing:-.2px}

  .hero{left:0;top:0;width:730px;height:348px;
    background:linear-gradient(180deg,#8fa5a0 0%,#5f8353 30%,#4f7440 55%,#8c8466 80%,#6e6650 100%)}
  .nav{left:111px;top:12px;width:508px;height:50px;background:rgba(240,240,240,.96);border-left:2px solid var(--navy);border-right:2px solid var(--navy)}
  .brand{left:12px;top:14px;font-family:"Oswald",sans-serif;font-weight:500;font-size:17px;color:var(--navy);letter-spacing:.3px}
  .nav-home{left:253px;top:0;width:39px;height:56px;background:var(--navy);font-size:8px;color:var(--white);text-align:center;padding-top:20px}
  .nav-link{top:20px;font-size:8px;color:var(--navy)}
  .nav-quote{left:436px;top:18px;width:60px;height:16px;background:var(--navy);color:var(--white);font-size:8px;text-align:center;line-height:16px}
  .arrow{width:28px;height:28px;background:var(--green);display:flex;align-items:center;justify-content:center}

  .intro-map{left:111px;top:284px;width:126px;height:126px;background:var(--green)}
  .intro-text{left:237px;top:284px;width:255px;height:126px;background:var(--navy)}
  .intro-text h1{position:absolute;left:31px;top:34px;font-size:17px;line-height:19px;font-weight:400}
  .intro-text p{position:absolute;left:31px;top:79px;font-size:7px}
  .dots{left:496px;top:331px;display:flex;gap:5px}
  .dots span{width:12px;height:11px;background:var(--green);font-size:7px;text-align:center;line-height:11px;font-weight:700}
  .dots span.on{background:var(--navy)}

  .about{left:111px;top:410px;width:254px;height:126px;background:var(--navy);padding:18px 18px 0 19px}
  .about h2,.alone h2{font-size:14px;font-weight:500;margin-bottom:4px}
  .accent-g{color:var(--green)}
  .accent-n{color:var(--navy)}
  .about p{font-size:7.6px;line-height:9.4px}

  .tile{width:126px;height:126px;background:var(--white);padding:3px}
  .tile .photo{width:120px;height:100px}
  .tile .label{height:17px;margin-top:3px;font-family:"Oswald",sans-serif;font-size:8.5px;text-align:center;line-height:17px;text-transform:uppercase}
  .lab-g{background:var(--green)} .lab-n{background:var(--navy)}

  .band{left:0;top:728px;width:730px;height:305px;background:linear-gradient(180deg,#3c3d82 0%,#43458a 60%,#5a5c98 100%)}
  .alone{left:238px;top:666px;width:381px;height:126px;background:var(--green);padding:14px 16px 0 16px}
  .alone p{font-size:7.6px;line-height:9.4px}

  .avatar{left:334px;top:809px;width:62px;height:62px;border-radius:50%;border:3px solid #8a8cb8;background:radial-gradient(circle,#b9854e 0%,#7a2a2a 60%,#2b2b3a 100%)}
  .cta-title{left:0;top:884px;width:730px;text-align:center;font-size:15px}
  .cta-sub{left:0;top:908px;width:730px;text-align:center;font-size:8px}
  .cta-btn{left:305px;top:932px;width:121px;height:18px;background:var(--green);font-size:8.5px;text-align:center;line-height:18px}

  .footer{left:111px;top:970px;width:508px;height:202px;background:var(--green)}
  .col{position:absolute}
  .col h3{font-family:"Oswald",sans-serif;font-weight:500;font-size:9px;color:var(--navy);text-transform:uppercase;margin-bottom:8px}
  .col ul{list-style:none;font-size:5.6px;line-height:7.9px;text-transform:uppercase;margin-bottom:20px}
  .col li::before{content:"• "}
  .contact{font-size:5.6px;line-height:7.4px;font-weight:700;text-transform:uppercase}
  .foot-brand{font-family:"Oswald",sans-serif;font-weight:500;font-size:15px;color:var(--white);margin-bottom:14px;line-height:16px}
  .legal{left:111px;top:1172px;width:508px;height:28px;background:var(--navy);font-size:6px;text-align:center;line-height:28px}
</style>
</head>
<body>

<div class="abs hero" role="img" aria-label="Photograph of the Great Wall winding over green mountains"></div>

<nav class="abs nav">
  <div class="abs brand">Brellin Trade Partners</div>
  <div class="abs nav-home head">Home</div>
  <div class="abs nav-link head" style="left:302px">Product Categories</div>
  <div class="abs nav-link head" style="left:382px">About Us</div>
  <div class="abs nav-quote head">Request Quote</div>
</nav>

<div class="abs arrow" style="left:82px;top:164px"><svg width="10" height="12" viewBox="0 0 10 12"><path d="M7 1 2 6l5 5" fill="none" stroke="#fff" stroke-width="2"/></svg></div>
<div class="abs arrow" style="left:619px;top:164px"><svg width="10" height="12" viewBox="0 0 10 12"><path d="M3 1l5 5-5 5" fill="none" stroke="#fff" stroke-width="2"/></svg></div>

<div class="abs intro-map" role="img" aria-label="World map illustration with Asia office locations"></div>
<svg class="abs" style="left:237px;top:340px" width="6" height="12"><path d="M0 0 6 6 0 12Z" fill="#7a9339"/></svg>
<div class="abs intro-text">
  <h1 class="head">Asian Outsourcing<br>Made Easy!</h1>
  <p>Custom Sewn Goods Made to Your Specifications</p>
</div>
<div class="abs dots"><span>1</span><span class="on">2</span><span>3</span><span>4</span><span>5</span><span>6</span></div>

<section class="abs about">
  <h2 class="head">Sourcing Custom <span class="accent-g">Goods in China</span></h2>
  <p>We outsource sewing services direct from China. Our long-established and extensive network of offshore factory-partners provides our clients with access to a wide variety of contract sewing expertise from Chinese manufacturers. Clients only need to communicate with our US agents, but will have the benefits of the cost savings &amp; quality workmanship from offshore outsourcing from Asia.</p>
</section>

<div class="abs tile" style="left:365px;top:410px"><div class="photo" role="img" aria-label="Photo of red fabric under a sewing machine" style="background:linear-gradient(160deg,#e7e3e0,#d23a3a)"></div><div class="label lab-g">Sewn Goods</div></div>
<div class="abs tile" style="left:492px;top:410px"><div class="photo" role="img" aria-label="Photo of a messenger bag" style="background:radial-gradient(circle,#4a4a4a 40%,#fff 75%)"></div><div class="label lab-n">Bags</div></div>
<div class="abs tile" style="left:111px;top:537px"><div class="photo" role="img" aria-label="Photo of a pair of ski gloves" style="background:radial-gradient(circle,#9a9a9a 35%,#fff 70%)"></div><div class="label lab-g">Gloves</div></div>
<div class="abs tile" style="left:238px;top:537px"><div class="photo" role="img" aria-label="Photo of a motorcycle cover" style="background:radial-gradient(ellipse,#2c3f8f 40%,#fff 72%)"></div><div class="label lab-n">Covers</div></div>
<div class="abs tile" style="left:365px;top:537px"><div class="photo" role="img" aria-label="Photo of colourful phone cases" style="background:linear-gradient(90deg,#222,#2a55c8,#7a3aa8,#e03a6a,#e23a2a,#e8a02a)"></div><div class="label lab-g">Cases</div></div>
<div class="abs tile" style="left:492px;top:537px"><div class="photo" role="img" aria-label="Photo of a medical pad" style="background:radial-gradient(ellipse,#cfd8ea 40%,#fff 72%)"></div><div class="label lab-n">Medical</div></div>

<div class="abs band" role="img" aria-label="Blue-tinted photo of a Chinese palace courtyard"></div>

<div class="abs tile" style="left:111px;top:666px"><div class="photo" role="img" aria-label="Photo of golf bags" style="background:radial-gradient(circle,#c0262a 30%,#333 55%,#fff 75%)"></div><div class="label lab-g">Sporting Goods</div></div>
<section class="abs alone">
  <h2 class="head">Don't Go at It <span class="accent-n">Alone!</span></h2>
  <p>Brellin Trade Partners has been sourcing custom sewn goods in Asia since 1998. We work with our clients by matching their unique production needs with the best possible China sewing factories. We manage the entire process from start to finish, by first identifying the best factories to quote each job. The next step is negotiating the best (fair) price possible. We complete the process by monitoring the quality of the goods during production, and then managing the ocean logistics, customs clearances and local delivery right to your door. Our services and our total commitment to customer satisfaction help level the playing field by giving our customers access to low cost, high quality China contract sewing.</p>
</section>

<div class="abs avatar" role="img" aria-label="Portrait photo of the company founder"></div>
<div class="abs arrow" style="left:82px;top:869px"><svg width="10" height="12" viewBox="0 0 10 12"><path d="M7 1 2 6l5 5" fill="none" stroke="#fff" stroke-width="2"/></svg></div>
<div class="abs arrow" style="left:619px;top:869px"><svg width="10" height="12" viewBox="0 0 10 12"><path d="M3 1l5 5-5 5" fill="none" stroke="#fff" stroke-width="2"/></svg></div>
<div class="abs cta-title head">Outsource Your Sewing Needs to Trusted Contractors in China</div>
<div class="abs cta-sub">Please contact us for immediate consultation regarding your outsourcing project.</div>
<div class="abs cta-btn head">Request Quote</div>

<footer class="abs footer">
  <div class="col" style="left:17px;top:22px">
    <h3>Custom Bags</h3>
    <ul><li>Athletic Bags</li><li>Backpacks</li><li>Computer Bags</li><li>Cooler Bags</li><li>Cosmetic Bags</li><li>Handbags</li><li>Messenger Bags</li><li>Shopping Bags</li><li>Tool Bags</li><li>Travel Bags</li><li>Yoga Bags</li></ul>
    <h3>Custom Cases</h3>
    <ul><li>Cosmetic Cases</li><li>Phone Cases</li><li>Tool Bags and Tool Cases</li></ul>
  </div>
  <div class="col" style="left:127px;top:22px">
    <h3>Custom Covers</h3>
    <ul><li>ATV Covers</li><li>Chair Covers</li><li>Equipment Covers</li><li>Golf Cart Covers</li><li>Motorcycle Covers</li><li>Outdoor Furniture Covers</li><li>Outdoor Grill Cover</li><li>Personal Watercraft Covers</li><li>Snowmobile Covers</li></ul>
    <h3 style="margin-top:6px">Custom Gloves</h3>
    <ul><li>Batting Gloves</li><li>Garden Gloves</li><li>Mechanic Gloves</li><li>Safety Gloves</li><li>Ski Gloves</li></ul>
  </div>
  <div class="col" style="left:253px;top:22px">
    <h3>Custom Medical Accessories</h3>
    <ul><li>Medical Equipment Covers</li><li>Medical Pads</li><li>Medical Sheets &amp; Bedding Supplies</li><li>Oxygen Tank Cases and Bags</li></ul>
    <h3>Custom Sewn Goods</h3>
    <ul><li>Pet Collars, Leashes, &amp; Harnesses</li><li>Socks</li></ul>
    <h3>Custom Sporting Goods</h3>
    <ul><li>Yoga Mats</li><li>Yoga Gear and Accessories</li></ul>
  </div>
  <div class="col" style="left:380px;top:18px;width:120px">
    <div class="foot-brand">Brellin Trade Partners</div>
    <p class="contact">US Headquarters</p>
    <p class="contact" style="margin-top:7px">Brellin Trade Partners, LLC<br>12 Harbor Lane<br>Suite 4<br>Dover, NH 03820</p>
    <p class="contact" style="margin-top:7px">Online: Inquiry Form<br>Tel: 555-010-4815<br>Fax: 555-010-4383<br>Email: info@brellintrade.example</p>
  </div>
</footer>
<div class="abs legal">© Brellin Trade Partners, LLC. | USA - Hong Kong - Taipei</div>

</body>
</html>
```